Pizza Snack Pack Design

The design of sleeve for “Crumb Carnival” packs, this is a tray of cheese & pizza flavored snack bread.
Sleeve covers the tray and offers two circular windows on the sleeve to show the cheese and snack bread.
With this project we are looking to convey to consumer that he/she is having pizza snack.
This is for the convenience or “food to go” section of the stores.

We have the information that will be printed on the base of the pack including ingredients, pack weight, bar code etc. it is important for the designer to focus on the top and side panels.
There is no limit to the number of colors can be used as we will be printing full color.

Target Market(s)

Any pizza loving person, 12 years and above, office workers, travelers, university students
Convenience stores, shops at airports, train stations, petrol stations.

Industry/Entity Type

Printing

Font styles to use
Serif
Sans Serif
Decorative
Script

Requirements
Must have
• Design for the sleeve on tray containing dip & snack bread that offers two windows to show the contents.
• The sleeve dimension The width is 158mm and Height is 181mm that includes 20mm overlap.
• The tray dimension: L: 160mm W: 75mm H: 27mm.
• Note: The design is more important than getting the dimension correct. All emphasis should be on the top and side panels. We will add the content details in-house.
Nice to have
• Strong emphasis on pizza flavor of the snack pack.
• Re-design of the pack name i.e. the Crumb Carnival writing to suit the new design.
Should not have
• Avoid clatter of shapes and writing and color clash.
• The design must tell the content within 10 second of consumer looking at it.

```html
<!DOCTYPE html>
<html lang="en">
<head>
<meta charset="utf-8">
<title>Crumb Carnival – Snack Pack Sleeve</title>
<link rel="stylesheet" href="https://fonts.googleapis.com/css2?family=Great+Vibes&family=Marck+Script&display=swap">
<style>
  :root {
    --page: #ecebe7;
    --leaf-green: #7cb23a;
    --leaf-green-light: #8cc043;
    --forest-green: #1f6b2e;
    --bark: #3a2214;
    --bark-dark: #1c100a;
    --bark-mid: #4a2c1b;
    --bark-light: #654030;
    --cream: #f1dfc2;
    --white: #ffffff;
    --crust: #e38a45;
    --crust-light: #f6c48f;
    --topping-red: #c8553a;
    --herb-green: #5e8f3a;
    --bread-pale: #eee4bf;
    --bread-gold: #c9b06e;
    --label: #efece6;
    --label-ink: #7a2a1e;
  }
  html, body {
    margin: 0;
    width: 1200px;
    height: 900px;
    overflow: hidden;
    background: var(--page);
  }
  .sleeve {
    position: absolute;
    left: 100px;
    top: 130px;
    width: 1000px;
  }
  .sleeve svg { display: block; }
  .brand-title {
    font-family: "Great Vibes", cursive;
    fill: var(--white);
    stroke: var(--forest-green);
    stroke-width: 1.4px;
    paint-order: stroke;
  }
  .brand-title--side { stroke: var(--bark-dark); }
  .tagline {
    font-family: "Marck Script", cursive;
    fill: #24401a;
  }
  .maker-name {
    font-family: "Marck Script", cursive;
    fill: var(--white);
  }
</style>
</head>
<body>
<main class="sleeve">

  <!-- Top panel -->
  <svg class="top-panel" width="1000" height="400" viewBox="0 0 1000 400">
    <defs>
      <linearGradient id="woodTone" x1="0" y1="0" x2="0.15" y2="1">
        <stop offset="0" stop-color="var(--bark-dark)"/>
        <stop offset=".12" stop-color="var(--bark-mid)"/>
        <stop offset=".25" stop-color="var(--bark)"/>
        <stop offset=".38" stop-color="var(--bark-light)"/>
        <stop offset=".5" stop-color="var(--bark)"/>
        <stop offset=".62" stop-color="var(--bark-mid)"/>
        <stop offset=".75" stop-color="var(--bark-light)"/>
        <stop offset=".88" stop-color="var(--bark)"/>
        <stop offset="1" stop-color="var(--bark-mid)"/>
      </linearGradient>
      <linearGradient id="grassTone" x1="0" y1="0" x2="0" y2="1">
        <stop offset="0" stop-color="var(--leaf-green-light)"/>
        <stop offset="1" stop-color="var(--leaf-green)"/>
      </linearGradient>
      <linearGradient id="dipTone" x1="0" y1="0" x2="0" y2="1">
        <stop offset="0" stop-color="var(--label)"/>
        <stop offset=".18" stop-color="var(--herb-green)"/>
        <stop offset=".32" stop-color="var(--topping-red)"/>
        <stop offset=".45" stop-color="var(--label)"/>
        <stop offset=".6" stop-color="var(--label-ink)"/>
        <stop offset=".72" stop-color="var(--label)"/>
        <stop offset="1" stop-color="#ddd6c8"/>
      </linearGradient>
      <radialGradient id="breadTone" cx=".4" cy=".4" r=".7">
        <stop offset="0" stop-color="var(--bread-pale)"/>
        <stop offset=".6" stop-color="#ddcf9f"/>
        <stop offset="1" stop-color="var(--bread-gold)"/>
      </radialGradient>
      <radialGradient id="snackTone" cx=".5" cy=".35" r=".65">
        <stop offset="0" stop-color="#b98a5c"/>
        <stop offset=".35" stop-color="var(--topping-red)"/>
        <stop offset=".6" stop-color="var(--crust)"/>
        <stop offset="1" stop-color="var(--crust-light)"/>
      </radialGradient>
    </defs>

    <rect class="panel-base" width="1000" height="400" fill="var(--leaf-green)"/>
    <polygon class="dark-strip" points="0,95 1000,0 1000,40 0,135" fill="var(--bark-dark)"/>
    <polygon class="wood-band" points="0,125 1000,30 1000,250 0,365" fill="url(#woodTone)"
             role="img" aria-label="Dark wood grain texture"/>
    <polygon class="grass-band" points="0,365 1000,250 1000,400 0,400" fill="url(#grassTone)"/>

    <g class="maker-mark">
      <rect x="58" y="0" width="62" height="58" fill="var(--forest-green)"/>
      <text class="maker-name" x="89" y="25" font-size="14" text-anchor="middle">Harvest</text>
      <text class="maker-name" x="89" y="44" font-size="14" text-anchor="middle">Lane</text>
    </g>

    <g class="window window--dip">
      <circle cx="265" cy="175" r="126" fill="none" stroke="var(--leaf-green)" stroke-width="3"/>
      <circle cx="265" cy="175" r="118" fill="var(--white)"/>
      <circle cx="265" cy="175" r="110" fill="url(#dipTone)"
              role="img" aria-label="Window showing the tomato and herb dip pot with its label"/>
    </g>

    <g class="window window--bread">
      <circle cx="762" cy="168" r="126" fill="none" stroke="var(--leaf-green)" stroke-width="3"/>
      <circle cx="762" cy="168" r="118" fill="var(--white)"/>
      <circle cx="762" cy="168" r="110" fill="url(#breadTone)"
              role="img" aria-label="Window showing golden cheese and pizza snack bread slices"/>
    </g>

    <ellipse class="hero-snack" cx="505" cy="240" rx="82" ry="72" fill="url(#snackTone)"
             role="img" aria-label="Toasted bread snack topped with tomato and herbs"/>

    <g transform="rotate(-5 560 70)">
      <text class="brand-title" x="520" y="62" font-size="46" text-anchor="middle">Crumb</text>
      <text class="brand-title" x="580" y="108" font-size="52" text-anchor="middle">Carnival</text>
    </g>

    <g transform="rotate(-5 800 330)">
      <text class="tagline" x="660" y="330" font-size="23">A tasty snack</text>
      <text class="tagline" x="730" y="362" font-size="23">for any time of the day</text>
    </g>
  </svg>

  <!-- Side panel -->
  <svg class="side-panel" width="1000" height="160" viewBox="0 0 1000 160">
    <rect width="1000" height="160" fill="var(--leaf-green)"/>
    <polygon class="bark-band" points="0,140 1000,22 1000,160 0,160" fill="var(--bark)"/>
    <polygon class="cream-band" points="430,160 1000,80 1000,160" fill="var(--cream)"/>

    <g transform="rotate(-5 200 80)">
      <text class="tagline" x="45" y="68" font-size="25">a tasty snack</text>
      <text class="tagline" x="45" y="102" font-size="25">for any time of the day</text>
    </g>

    <g transform="rotate(-5 560 90)">
      <text class="brand-title brand-title--side" x="520" y="70" font-size="50" text-anchor="middle">Crumb</text>
      <text class="brand-title brand-title--side" x="570" y="122" font-size="56" text-anchor="middle">Carnival</text>
    </g>
  </svg>

</main>
</body>
</html>
```